Marks of Dunmore business card design

I need a clean, professional looking design using the attached logo with a bright green/ gray/dark gray/black colors. Maybe even an orange accent if it looks good. I am open to slight changes in the logo if needed. Details below on the info on what should be on the cards. We are a sign company in Ft. Lauderdale FL that specializes in yacht lettering on multi million dollar yachts.

Target Market(s)

marine industry, yachts

Industry/Entity Type

Business

Colors
9bcb3c
000000
606060
f37122

Requirements
Must have
• address: 4837 W. Tallow Rd.
• Alder Cove, GA 31520
• Phone: 555-518-4062
• email/website: marksofdunmore@postvane.com MarksofDunmore.com
Nice to have
• I would like it very clean and simple but professional looking. Nice layout and would prefer a darker background. Orange highlight only if it works.
Should not have
• Nothing fancy.

```html
<!DOCTYPE html>
<html lang="en">
<head>
<meta charset="utf-8">
<title>Marks of Dunmore business card</title>
<link href="https://fonts.googleapis.com/css2?family=Work+Sans:wght@400;500;700&display=swap" rel="stylesheet">
<style>
  :root {
    --green: #0f9138;
    --orange: #f37122;
    --black: #151515;
    --ink: #2a2a2a;
    --grey: #555555;
    --white: #ffffff;
    --backdrop: #e4e4e4;
  }
  * { margin: 0; padding: 0; box-sizing: border-box; }
  html, body {
    width: 1200px; height: 1000px; overflow: hidden;
    background: var(--backdrop);
    font-family: "Work Sans", Arial, sans-serif;
  }
  .canvas { position: relative; width: 1200px; height: 1000px; }
  .card {
    position: absolute; left: 240px; width: 697px;
    border-radius: 22px; overflow: hidden;
    box-shadow: 0 6px 14px rgba(0,0,0,0.18);
  }
  .card-front { top: 83px; height: 395px; background: var(--white); }
  .card-back { top: 520px; height: 397px; background: var(--black); }

  .brand-name {
    position: absolute; color: var(--green);
    font-weight: 700; white-space: nowrap; letter-spacing: 0.5px;
  }
  .card-front .brand-name { left: 42px; top: 58px; font-size: 42px; }
  .card-back .brand-name {
    left: 0; right: 0; top: 170px; text-align: center; font-size: 50px;
  }

  .person { position: absolute; right: 37px; top: 208px; text-align: right; }
  .person-name {
    color: var(--green); font-size: 24px; font-weight: 400;
    letter-spacing: 1.5px; text-transform: uppercase;
  }
  .person-title { color: var(--ink); font-size: 14px; letter-spacing: 1px; margin-top: 6px; }

  .divider {
    position: absolute; left: 42px; right: 39px; top: 276px;
    height: 1.5px; background: var(--orange);
  }

  .address {
    position: absolute; left: 42px; top: 292px;
    color: var(--grey); font-size: 15px; line-height: 20px;
  }
  .contacts {
    position: absolute; right: 36px; top: 292px;
    list-style: none; color: var(--grey); font-size: 15px; line-height: 20px;
  }
  .contacts li { display: flex; align-items: center; justify-content: flex-end; gap: 12px; }
  .contacts svg { width: 10px; height: 10px; flex: none; }

  .front-band { position: absolute; left: 0; bottom: 0; width: 697px; height: 32px; }

  .back-web {
    position: absolute; left: 0; right: 0; top: 345px; text-align: center;
    color: var(--white); font-size: 16px; letter-spacing: 2px;
  }
  .back-web .accent { color: var(--green); }
</style>
</head>
<body>
<div class="canvas">
  <section class="card card-front">
    <div class="brand-name">Marks of Dunmore</div>
    <div class="person">
      <div class="person-name">Daniel Hartley</div>
      <div class="person-title">CEO</div>
    </div>
    <div class="divider"></div>
    <div class="address">4837 W. Tallow Rd.<br>Alder Cove, GA 31520</div>
    <ul class="contacts">
      <li>555-518-4062
        <svg viewBox="0 0 10 10"><path d="M2 1 L4 1 L4.6 3 L3.4 3.8 Q4.2 5.8 6.2 6.6 L7 5.4 L9 6 L9 8 Q5 9 2.4 6.4 Q0.6 4 2 1 Z" fill="var(--green)"/></svg>
      </li>
      <li>marksofdunmore@postvane.com
        <svg viewBox="0 0 10 10"><rect x="1" y="2.2" width="8" height="5.6" fill="none" stroke="var(--green)" stroke-width="1.1"/><path d="M1 2.4 L5 5.4 L9 2.4" fill="none" stroke="var(--green)" stroke-width="1.1"/></svg>
      </li>
      <li>www.MarksofDunmore.com
        <svg viewBox="0 0 10 10"><circle cx="5" cy="5" r="4" fill="none" stroke="var(--green)" stroke-width="1"/><path d="M1 5 H9 M5 1 Q2.5 5 5 9 M5 1 Q7.5 5 5 9" fill="none" stroke="var(--green)" stroke-width="0.9"/></svg>
      </li>
    </ul>
    <svg class="front-band" viewBox="0 0 697 32" preserveAspectRatio="none" aria-hidden="true">
      <path d="M0 11 L392 11 C398 11 402 12 406 15 L402 16 C398 16 396 16 392 16 L0 16 Z" fill="var(--black)"/>
      <path d="M0 20 L396 20 C418 20 424 3 452 3 L697 3 L697 32 L0 32 Z" fill="var(--green)"/>
    </svg>
  </section>

  <section class="card card-back">
    <div class="brand-name">Marks of Dunmore</div>
    <div class="back-web">www.<span class="accent">MarksofDunmore</span>.com</div>
  </section>
</div>
</body>
</html>
```